Bright acorns day nursery pkr limited

we would like create a website that can be updated by us easily as we have regular changes to what we provide and need. we would like something that is classy but also appealing from a child's aspect. we would be looking to add our own logo and our edvarn logo both attached, if you guys can create it and we will work with the preferred choice to add all the text.
We would like the links to nest ledger, edvarn report and our chatterly feed on the front page

we are looking for a website for our childcare business we have 2 nurseries that we would like one website.
showing our opening hours, price list, policies etc as well as photos, description of our day, staff photos and their training accreditation's.

Target Market(s)

Families

Industry/Entity Type

Childcare

Number of Pages Required

5+ page

Font styles to use
Serif

Colors

Designer to choose colors to be used in the design.

Requirements
Must have
• links to social media and other websites, photographs, links to download registration forms etc, parents able to leave reviews. zarloo charts link, job opportunities
Nice to have
• facilities to take payments

```html
<!DOCTYPE html>
<html lang="en">
<head>
<meta charset="utf-8">
<title>Bright Acorns Day Nursery</title>
<link href="https://fonts.googleapis.com/css2?family=Lilita+One&family=Open+Sans:wght@400;600;700;800&family=Playfair+Display:wght@700;900&family=Dancing+Script:wght@700&display=swap" rel="stylesheet">
<style>
:root{
  --blue:#0d3b85;
  --blue-dark:#0a2c66;
  --pink:#c8157a;
  --pink-light:#e0509c;
  --green:#4fae3a;
  --green-dark:#3f9a2d;
  --ink:#333333;
  --muted:#666666;
  --line:#d8d8d8;
  --paper:#ffffff;
  --page:#f6f6f6;
  --night:#1b1f2e;
}
*{box-sizing:border-box;margin:0;padding:0}
html,body{width:1200px;height:4423px;overflow:hidden}
body{font-family:"Open Sans",Arial,sans-serif;color:var(--ink);background:var(--paper);font-size:13px;line-height:1.5}
.wrap{width:860px;margin:0 auto;position:relative}
section,header,nav,footer{position:relative}
.zig{position:absolute;left:0;width:1200px;height:12px;z-index:5;display:block}
.zig.bottom{bottom:-12px}
.zig.top{top:-12px}
.btn{display:inline-flex;align-items:center;gap:8px;font-weight:700;font-size:12px;letter-spacing:.5px;text-transform:uppercase;color:#fff;text-decoration:none;padding:0 18px;height:40px;border-radius:3px}
.btn-pink{background:var(--pink)}
.btn-blue{background:var(--blue)}
.btn svg{width:14px;height:14px}
.photo{display:block}

/* header */
.site-header{height:88px;background:#fff}
.site-header .wrap{display:flex;justify-content:space-between;align-items:center;height:88px}
.brand{display:flex;align-items:center;gap:12px;text-decoration:none}
.brand-dot{width:40px;height:40px;border-radius:50%;background:var(--pink)}
.brand-name{font-family:"Lilita One",sans-serif;color:var(--blue);font-size:22px;line-height:1.05;text-transform:uppercase}
.call{text-align:right}
.call-label{display:flex;align-items:center;justify-content:flex-end;gap:8px;color:var(--muted);font-size:16px}
.call-label svg{width:20px;height:20px}
.call-number{font-family:"Open Sans",sans-serif;font-weight:800;color:var(--blue);font-size:34px;line-height:1.1;letter-spacing:.5px}

/* nav */
.main-nav{height:42px;background:var(--pink)}
.main-nav ul{list-style:none;display:flex;height:42px;align-items:stretch;justify-content:space-between}
.main-nav a{display:flex;align-items:center;height:42px;padding:0 16px;color:#fff;text-decoration:none;font-weight:700;font-size:12px;letter-spacing:.3px}
.main-nav .active a{background:var(--pink-light)}

/* hero */
.hero{height:520px;background:linear-gradient(110deg,#c98f6d 0%,#e7c2a4 30%,#b9cbe0 55%,#6b93bf 75%,#d8b492 100%)}
.hero-label{position:absolute;left:398px;top:425px;width:414px;height:95px;background:var(--green);text-align:center;color:#fff;font-family:"Lilita One",sans-serif;text-transform:uppercase;padding-top:14px}
.hero-label .small{font-size:20px;line-height:1}
.hero-label .big{font-size:46px;line-height:1.1}

/* funding */
.funding{height:370px;background:var(--blue);color:#fff;text-align:center;padding-top:40px}
.funding .kicker{font-family:"Lilita One",sans-serif;font-size:36px;letter-spacing:1px;line-height:1.2}
.funding h2{font-family:"Playfair Display",Georgia,serif;font-weight:900;font-size:58px;letter-spacing:1.5px;line-height:1.1;margin-top:6px}
.funding p{font-size:14px;line-height:1.85;margin-top:30px}
.funding .btn{margin-top:28px}

/* welcome */
.welcome{height:410px;background:#fff}
.welcome .wrap{display:flex;gap:30px;padding-top:65px}
.welcome-photo{width:428px;height:292px;background:linear-gradient(135deg,#d7a07f,#f1d3a5 45%,#9fc3e0 80%,#e58a8a);flex:none}
.welcome-text h2{font-family:"Lilita One",sans-serif;color:var(--pink);font-size:30px;line-height:1.1;text-transform:uppercase}
.welcome-text p{font-size:11.5px;line-height:1.55;color:var(--muted);margin-top:12px}
.welcome-text .btn{margin-top:20px;height:38px}

/* section heading */
.sec-title{font-family:"Lilita One",sans-serif;font-size:40px;text-align:center;text-transform:uppercase;line-height:1}
.sec-title::after{content:"";display:block;width:60px;height:4px;margin:12px auto 0;background:currentColor}

/* our day */
.our-day{height:458px;background:var(--pink);color:#fff;padding-top:52px}
.our-day .sec-title::after{background:#fff}
.day-grid{display:flex;justify-content:space-between;margin-top:38px}
.day-card{width:254px}
.day-photo{height:130px;border:4px solid #fff;background:linear-gradient(135deg,#8fb6dc,#f2c7a0 50%,#d06a6a)}
.day-card:nth-child(2) .day-photo{background:linear-gradient(135deg,#f3d56b,#e99c6f 50%,#6fa2d6)}
.day-card:nth-child(3) .day-photo{background:linear-gradient(135deg,#c5d6a3,#e7b491 50%,#8aa1c5)}
.day-card p{font-size:11.5px;line-height:1.5;margin-top:10px}
.more-link{display:inline-flex;align-items:center;gap:8px;margin-top:22px;color:#fff;text-decoration:none;font-family:"Lilita One",sans-serif;font-size:16px;letter-spacing:.5px}
.more-link svg{width:26px;height:26px}

/* price list */
.prices{height:633px;background:#fff;padding-top:50px;text-align:center}
.prices .sec-title{color:var(--green)}
.prices .sec-title::after{background:var(--pink)}
.prices .subtitle{color:var(--blue);font-weight:800;font-size:17px;margin-top:20px}
.price-table{width:864px;margin:14px auto 0;border-collapse:collapse;border:2px solid var(--blue);font-size:13px}
.price-table th{background:var(--blue);color:#fff;font-weight:700;font-size:19px;height:46px}
.price-table td{border:1px solid #b9c4d8;height:56px;font-size:17px;color:#222;line-height:1.3}
.price-table td.row-label{width:290px;font-size:15px;font-weight:700}
.price-table td.row-label small,.price-table td small{display:block;font-weight:400;font-size:12px;color:#444}
.price-notes{margin-top:28px;font-size:12px;line-height:1.7}
.price-notes .lead{color:var(--pink);font-weight:800;font-size:16px}
.price-notes .pinkline{color:var(--pink);font-weight:600}
.price-notes .plain{margin-top:16px;color:#333}

/* staff */
.staff{height:437px;background:var(--green);color:#fff;padding-top:40px}
.staff .sec-title{color:#fff}
.staff-grid{display:flex;justify-content:space-between;margin-top:26px}
.staff-card{width:210px;text-align:center}
.staff-photo{width:170px;height:170px;margin:0 auto;border-radius:50%;border:4px solid #fff;background:radial-gradient(circle at 50% 45%,#e9c6a8,#b88a6c 60%,#6f8fb5)}
.staff-card h3{font-size:13px;font-weight:700;margin-top:14px}
.staff-card p{font-size:11px;line-height:1.45;margin-top:6px}
.staff-card .btn{height:26px;padding:0 12px;font-size:10px;margin-top:14px}

/* gallery */
.gallery{height:728px;background:#fff;padding-top:50px}
.award{width:177px;height:177px;margin:0 auto;border-radius:50%;background:var(--blue);border:6px solid #dfe6f2}
.gallery .sec-title{color:#222;margin-top:46px}
.filters{display:flex;justify-content:center;gap:16px;margin-top:24px}
.filters a{width:100px;height:36px;display:flex;align-items:center;justify-content:center;border:1px solid var(--line);border-radius:18px;font-size:10px;font-weight:700;color:#999;text-decoration:none;letter-spacing:.5px}
.filters a.on{background:var(--pink);border-color:var(--pink);color:#fff}
.g-row{display:flex;justify-content:space-between;margin-top:20px;height:135px}
.g-row+.g-row{margin-top:20px}
.g-item{height:135px}
.g1{background:linear-gradient(120deg,#f3c06a,#e58d62 50%,#7aa6d4)}
.g2{background:linear-gradient(120deg,#f2d4b8,#a9c7e5)}
.g3{background:linear-gradient(120deg,#8fc7e8,#f0b38a 60%,#d96a6a)}
.g4{background:linear-gradient(120deg,#d9b08a,#88a9c7)}
.g5{background:linear-gradient(120deg,#e7a19c,#f3d2a9 50%,#b0cde3)}
.g6{background:linear-gradient(120deg,#c6e0f2,#f1c59a 60%,#e18a7c)}
.g7{background:linear-gradient(120deg,#f6d37a,#e68c6a 50%,#6e9ed0)}

/* policies */
.info-row{height:324px;background:#fff}
.info-row .wrap{display:flex;justify-content:space-between}
.policies{width:583px;height:280px;border:1px solid var(--line);box-shadow:0 2px 6px rgba(0,0,0,.1);display:flex;gap:26px;padding:26px 22px}
.policy-photo{width:168px;height:222px;flex:none;background:linear-gradient(160deg,#cfd6de,#b68a6d 55%,#3a4a63)}
.policies h2{font-family:"Lilita One",sans-serif;font-size:22px;color:#222;text-transform:uppercase}
.policies h2::after{content:"";display:block;width:40px;height:3px;background:var(--pink);margin-top:6px}
.policies p{font-size:11px;line-height:1.5;color:var(--muted);margin-top:10px}
.policies .btn{height:30px;font-size:10px;padding:0 12px;margin-top:14px}
.social-box{width:236px;height:280px;border:1px solid var(--line);background:#fff}
.social-head{height:44px;background:#3b5a98;color:#fff;display:flex;align-items:center;gap:10px;padding:0 14px;font-weight:700;font-size:14px}
.social-head span.sq{width:18px;height:18px;background:#fff;border-radius:2px;flex:none}
.social-page{display:flex;gap:8px;padding:10px;font-size:11px;font-weight:700;color:#3b5a98}
.social-page .thumb{width:40px;height:40px;background:#e8ecf4;flex:none}
.social-grid{margin:0 10px;height:150px;background:linear-gradient(135deg,#c9d3e4,#e7c9b3 50%,#a9bfd9)}
.social-foot{font-size:9px;color:#888;padding:8px 10px}

/* contact */
.contact{height:325px;background:linear-gradient(180deg,var(--blue) 0%,#1a2d5c 30%,var(--night) 100%);padding-top:60px}
.contact .wrap{display:flex;height:250px}
.map{width:563px;height:250px;background:linear-gradient(135deg,#e9e4d8,#cfdcc0 40%,#f0e9d2 60%,#b7cbe0)}
.contact-card{flex:1;background:var(--pink);color:#fff;padding:18px 22px}
.contact-card h2{font-family:"Lilita One",sans-serif;font-size:40px;line-height:1;text-transform:uppercase}
.c-item{display:flex;gap:8px;margin-top:12px;font-size:11px;line-height:1.4}
.c-item svg{width:14px;height:14px;flex:none;margin-top:1px}
.c-item b{display:block;font-size:12px;text-transform:uppercase}

/* footer */
.site-footer{height:88px;background:var(--night);color:#ccc}
.site-footer .wrap{display:flex;justify-content:space-between;align-items:center;height:88px}
.foot-links{list-style:none;display:flex;gap:16px;font-size:10px;font-weight:600}
.foot-links a{color:#ddd;text-decoration:none}
.copy{font-size:10px;color:#999;margin-top:8px}
.follow{display:flex;align-items:center;gap:8px}
.follow span{font-family:"Dancing Script",cursive;font-size:26px;color:#fff;margin-right:6px}
.follow i{width:24px;height:24px;border-radius:50%;background:#fff;display:block}
</style>
</head>
<body>

<svg width="0" height="0" style="position:absolute" aria-hidden="true">
  <defs>
    <pattern id="zig-blue-down" width="16" height="12" patternUnits="userSpaceOnUse"><path d="M0 0L8 12L16 0Z" fill="#0d3b85"/></pattern>
    <pattern id="zig-pink-up" width="16" height="12" patternUnits="userSpaceOnUse"><path d="M0 12L8 0L16 12Z" fill="#c8157a"/></pattern>
    <pattern id="zig-pink-down" width="16" height="12" patternUnits="userSpaceOnUse"><path d="M0 0L8 12L16 0Z" fill="#c8157a"/></pattern>
    <pattern id="zig-green-up" width="16" height="12" patternUnits="userSpaceOnUse"><path d="M0 12L8 0L16 12Z" fill="#4fae3a"/></pattern>
    <pattern id="zig-green-down" width="16" height="12" patternUnits="userSpaceOnUse"><path d="M0 0L8 12L16 0Z" fill="#4fae3a"/></pattern>
  </defs>
</svg>

<header class="site-header">
  <div class="wrap">
    <a class="brand" href="#">
      <span class="brand-dot"></span>
      <span class="brand-name">Bright Acorns<br>Day Nursery</span>
    </a>
    <div class="call">
      <div class="call-label">
        <svg viewBox="0 0 24 24" fill="none" stroke="#0d3b85" stroke-width="2"><path d="M5 3h4l2 5-2.5 1.5a11 11 0 0 0 6 6L16 13l5 2v4a2 2 0 0 1-2 2A16 16 0 0 1 3 5a2 2 0 0 1 2-2z"/></svg>
        Call Us for childcare
      </div>
      <div class="call-number">555-014-2290</div>
    </div>
  </div>
</header>

<nav class="main-nav">
  <div class="wrap">
    <ul>
      <li class="active"><a href="#">HOME</a></li>
      <li><a href="#">ABOUT US</a></li>
      <li><a href="#">PRICE LIST</a></li>
      <li><a href="#">OUR STAFF</a></li>
      <li><a href="#">CHILDCARE</a></li>
      <li><a href="#">COMMUNITY</a></li>
      <li><a href="#">GALLERY</a></li>
      <li><a href="#">POLICIES</a></li>
      <li><a href="#">CONTACT US</a></li>
    </ul>
  </div>
</nav>

<section class="hero" role="img" aria-label="Photo of a smiling nursery teacher threading beads with two young children">
  <div class="hero-label">
    <div class="small">Bright Acorns</div>
    <div class="big">Day Nursery</div>
  </div>
</section>

<section class="funding">
  <div class="kicker">IS YOU CHILD</div>
  <h2>ENTITLED TO FUNDING?</h2>
  <p>Do you meet the 2 year funding criteria?<br>
  To apply please take an application form from our leaflet holders outside the main nursery door.<br>
  All 3 year old children receive 15 hours free government funding from the term after their 3rd birthday!<br>
  Check out the government website for 30 hours free childcare from September 2017.</p>
  <a class="btn btn-pink" href="#">READ MORE
    <svg viewBox="0 0 16 16"><circle cx="8" cy="8" r="7" fill="#fff"/><path d="M7 5l3 3-3 3" stroke="#c8157a" stroke-width="2" fill="none"/></svg>
  </a>
  <svg class="zig bottom" viewBox="0 0 1200 12" preserveAspectRatio="none" aria-hidden="true"><rect width="1200" height="12" fill="url(#zig-blue-down)"/></svg>
</section>

<section class="welcome">
  <div class="wrap">
    <div class="welcome-photo photo" role="img" aria-label="Photo of a teacher and three children playing with colourful toys"></div>
    <div class="welcome-text">
      <h2>Welcome to Bright Acorns</h2>
      <p>Lorem Ipsum is simply dummy text of the printing and typesetting industry. Lorem Ipsum has been the industry's standard dummy text ever since the 1500s, when an unknown printer took a galley of type and scrambled it to make a type specimen book. It has survived not only five centuries, but also the leap into electronic typesetting, remaining essentially unchanged.</p>
      <p>Lorem Ipsum is simply dummy text of the printing and typesetting industry. It was popularised in the 1960s with the release of sheets containing Lorem Ipsum passages, and more recently with desktop publishing software including versions of Lorem Ipsum.</p>
      <a class="btn btn-blue" href="#">READ MORE
        <svg viewBox="0 0 16 16"><circle cx="8" cy="8" r="7" fill="#fff"/><path d="M7 5l3 3-3 3" stroke="#0d3b85" stroke-width="2" fill="none"/></svg>
      </a>
    </div>
  </div>
</section>

<section class="our-day">
  <svg class="zig top" viewBox="0 0 1200 12" preserveAspectRatio="none" aria-hidden="true"><rect width="1200" height="12" fill="url(#zig-pink-up)"/></svg>
  <div class="wrap">
    <h2 class="sec-title">Our Day</h2>
    <div class="day-grid">
      <article class="day-card">
        <div class="day-photo photo" role="img" aria-label="Photo of children doing crafts at a table"></div>
        <p>Lorem Ipsum is simply dummy text of the printing and typesetting industry. It has survived not only five centuries, but also the leap into electronic typesetting, remaining essentially unchanged.</p>
        <a class="more-link" href="#">READ MORE <svg viewBox="0 0 26 26"><circle cx="13" cy="13" r="11" fill="none" stroke="#fff" stroke-width="2"/><path d="M11 8l5 5-5 5" stroke="#fff" stroke-width="2" fill="none"/></svg></a>
      </article>
      <article class="day-card">
        <div class="day-photo photo" role="img" aria-label="Photo of smiling children in a classroom"></div>
        <p>Lorem Ipsum is simply dummy text of the printing and typesetting industry. It has survived not only five centuries, but also the leap into electronic typesetting, remaining essentially unchanged.</p>
        <a class="more-link" href="#">READ MORE <svg viewBox="0 0 26 26"><circle cx="13" cy="13" r="11" fill="none" stroke="#fff" stroke-width="2"/><path d="M11 8l5 5-5 5" stroke="#fff" stroke-width="2" fill="none"/></svg></a>
      </article>
      <article class="day-card">
        <div class="day-photo photo" role="img" aria-label="Photo of a group of children standing together"></div>
        <p>Lorem Ipsum is simply dummy text of the printing and typesetting industry. It has survived not only five centuries, but also the leap into electronic typesetting, remaining essentially unchanged.</p>
        <a class="more-link" href="#">READ MORE <svg viewBox="0 0 26 26"><circle cx="13" cy="13" r="11" fill="none" stroke="#fff" stroke-width="2"/><path d="M11 8l5 5-5 5" stroke="#fff" stroke-width="2" fill="none"/></svg></a>
      </article>
    </div>
  </div>
  <svg class="zig bottom" viewBox="0 0 1200 12" preserveAspectRatio="none" aria-hidden="true"><rect width="1200" height="12" fill="url(#zig-pink-down)"/></svg>
</section>

<section class="prices">
  <h2 class="sec-title">Price List</h2>
  <div class="subtitle">NEW PRICE LIST FROM 1ST APRIL 2017</div>
  <table class="price-table">
    <thead>
      <tr><th></th><th>Under 2's</th><th>2-5's</th></tr>
    </thead>
    <tbody>
      <tr><td class="row-label">Half day<small>8am-1pm or 1pm-6pm</small></td><td>£26</td><td>£25</td></tr>
      <tr><td class="row-label">Full day<small>(7.30-6pm)</small></td><td>£40</td><td>£38</td></tr>
      <tr><td class="row-label">Full time<small>Mon- Fri 7.30-6pm</small></td><td>£168</td><td>£161<small>(Funded children in holidays)</small></td></tr>
      <tr><td class="row-label">Full time funded children<small>3+ years old*</small></td><td>xxxxxxxxxxx</td><td>£130<small>During term time</small></td></tr>
    </tbody>
  </table>
  <div class="price-notes">
    <div class="lead">FEES INCLUDE BREAKFAST (FULL DAY/FULL TIME ONLY)</div>
    <div class="pinkline">A LIGHT SNACK EACH SESSION, NAPPIES AND WIPES.</div>
    <div class="plain">MEALS CAN BE OFFERED FOR AN ADDITIONAL CHARGE (£2.50 PER MEAL, PER DAY).<br>PLEASE SEE A MEMBER OF STAFF!</div>
  </div>
</section>

<section class="staff">
  <svg class="zig top" viewBox="0 0 1200 12" preserveAspectRatio="none" aria-hidden="true"><rect width="1200" height="12" fill="url(#zig-green-up)"/></svg>
  <div class="wrap">
    <h2 class="sec-title">Our Staff</h2>
    <div class="staff-grid">
      <div class="staff-card">
        <div class="staff-photo photo" role="img" aria-label="Portrait photo of a staff member"></div>
        <h3>Mara Ellison</h3>
        <p>Lorem Ipsum is simply dummy text make a type specimen book. It has survived not only five centuries.</p>
        <a class="btn btn-pink" href="#">Read More</a>
      </div>
      <div class="staff-card">
        <div class="staff-photo photo" role="img" aria-label="Portrait photo of a staff member"></div>
        <h3>Mara Ellison</h3>
        <p>Lorem Ipsum is simply dummy text make a type specimen book. It has survived not only five centuries.</p>
        <a class="btn btn-pink" href="#">Read More</a>
      </div>
      <div class="staff-card">
        <div class="staff-photo photo" role="img" aria-label="Portrait photo of a staff member"></div>
        <h3>Mara Ellison</h3>
        <p>Lorem Ipsum is simply dummy text make a type specimen book. It has survived not only five centuries.</p>
        <a class="btn btn-pink" href="#">Read More</a>
      </div>
      <div class="staff-card">
        <div class="staff-photo photo" role="img" aria-label="Portrait photo of a staff member"></div>
        <h3>Mara Ellison</h3>
        <p>Lorem Ipsum is simply dummy text make a type specimen book. It has survived not only five centuries.</p>
        <a class="btn btn-pink" href="#">Read More</a>
      </div>
    </div>
  </div>
  <svg class="zig bottom" viewBox="0 0 1200 12" preserveAspectRatio="none" aria-hidden="true"><rect width="1200" height="12" fill="url(#zig-green-down)"/></svg>
</section>

<section class="gallery">
  <div class="award" role="img" aria-label="Edvarn inspection rating badge"></div>
  <h2 class="sec-title">Our Gallery</h2>
  <div class="filters">
    <a class="on" href="#">ALL</a>
    <a href="#">EVENT</a>
    <a href="#">PROGRAMS</a>
    <a href="#">TEACHERS</a>
  </div>
  <div class="wrap">
    <div class="g-row">
      <div class="g-item g1" style="width:413px" role="img" aria-label="Gallery photo of children painting"></div>
      <div class="g-item g2" style="width:189px" role="img" aria-label="Gallery photo of toddlers playing on the floor"></div>
      <div class="g-item g3" style="width:191px" role="img" aria-label="Gallery photo of a child with building blocks"></div>
    </div>
    <div class="g-row">
      <div class="g-item g4" style="width:171px" role="img" aria-label="Gallery photo of a teacher reading with a child"></div>
      <div class="g-item g5" style="width:213px" role="img" aria-label="Gallery photo of children at a play table"></div>
      <div class="g-item g6" style="width:189px" role="img" aria-label="Gallery photo of toddlers with toys"></div>
      <div class="g-item g7" style="width:191px" role="img" aria-label="Gallery photo of colourful building blocks"></div>
    </div>
  </div>
</section>

<section class="info-row">
  <div class="wrap">
    <div class="policies">
      <div class="policy-photo photo" role="img" aria-label="Portrait photo of the nursery manager"></div>
      <div>
        <h2>Our Policies</h2>
        <p>Lorem Ipsum is simply dummy text of the printing and typesetting industry. Lorem Ipsum has been the industry's standard dummy text ever since, when an unknown printer took a galley of type and scrambled it to make a type specimen book.</p>
        <p>Lorem Ipsum is simply dummy text of the printing and typesetting industry. Lorem Ipsum has been the industry's standard dummy text with desktop publishing software.</p>
        <a class="btn btn-pink" href="#">READ MORE
          <svg viewBox="0 0 16 16"><circle cx="8" cy="8" r="7" fill="#fff"/><path d="M7 5l3 3-3 3" stroke="#c8157a" stroke-width="2" fill="none"/></svg>
        </a>
      </div>
    </div>
    <aside class="social-box">
      <div class="social-head"><span class="sq"></span>Find us on Chatterly</div>
      <div class="social-page"><span class="thumb"></span>Bright Acorns Day Nursery</div>
      <div class="social-grid" role="img" aria-label="Grid of recent photos from the Chatterly feed"></div>
      <div class="social-foot">Chatterly social plugin</div>
    </aside>
  </div>
</section>

<section class="contact">
  <div class="wrap">
    <div class="map" role="img" aria-label="Zarloo charts map showing the nursery location"></div>
    <div class="contact-card">
      <h2>Contact Us</h2>
      <div class="c-item">
        <svg viewBox="0 0 16 16" fill="none" stroke="#fff" stroke-width="1.6"><circle cx="8" cy="8" r="6.5"/><path d="M8 4v4l3 2"/></svg>
        <div><b>Operating Hours:</b>Open Monday to Friday 7.30am to 6pm</div>
      </div>
      <div class="c-item">
        <svg viewBox="0 0 16 16" fill="#fff"><path d="M8 1a5 5 0 0 0-5 5c0 4 5 9 5 9s5-5 5-9a5 5 0 0 0-5-5zm0 7a2 2 0 1 1 0-4 2 2 0 0 1 0 4z"/></svg>
        <div><b>Address:</b>48 Orchard Lane, Fernwick, 4511</div>
      </div>
      <div class="c-item">
        <svg viewBox="0 0 16 16" fill="#fff"><path d="M3 1h3l1.5 3.5L5.5 6a8 8 0 0 0 4.5 4.5l1.5-2L15 10v3a2 2 0 0 1-2 2A12 12 0 0 1 1 3a2 2 0 0 1 2-2z"/></svg>
        <div><b>Telephone:</b>0400 118 274</div>
      </div>
      <div class="c-item">
        <svg viewBox="0 0 16 16" fill="none" stroke="#fff" stroke-width="1.6"><rect x="1.5" y="3.5" width="13" height="9"/><path d="M1.5 3.5L8 9l6.5-5.5"/></svg>
        <div><b>Email:</b>hello@brightacorns.example</div>
      </div>
    </div>
  </div>
</section>

<footer class="site-footer">
  <div class="wrap">
    <div>
      <ul class="foot-links">
        <li><a href="#">HOME</a></li>
        <li><a href="#">ABOUT US</a></li>
        <li><a href="#">PRICE LIST</a></li>
        <li><a href="#">OUR STAFF</a></li>
        <li><a href="#">CHILDCARE</a></li>
        <li><a href="#">COMMUNITY</a></li>
        <li><a href="#">CONTACT US</a></li>
      </ul>
      <div class="copy">© 2017 brightacorns.example. All rights reserved.</div>
    </div>
    <div class="follow"><span>Follow Us</span><i></i><i></i><i></i><i></i><i></i></div>
  </div>
</footer>

</body>
</html>
```